Eye-catching Card for new church

I would like a card the size of a business card ... that can be used to announce the start of our new church. I would like it to have our logo on the card, my name, and the statement "Coming Soon ... 1.10.2016". I also would like to list our website address and Facebook page and my Twitter account.

Target Market(s)

prospective people looking for a church

Industry/Entity Type

Church

Requirements
Must have
• a focus on Coming Soon ... 1.10.2016
• Brightfold Church logo
Should not have
• church buildings or writings on the cross

```html
<!DOCTYPE html>
<html lang="en">
<head>
<meta charset="utf-8">
<title>Brightfold Church — Coming Soon Card</title>
<link rel="stylesheet" href="https://fonts.googleapis.com/css2?family=Playfair+Display:wght@400&family=Arimo:wght@400;700&display=swap">
<style>
  :root {
    --sky-top: #0758ad;
    --sky-bottom: #1ea1ea;
    --paper: #ffffff;
    --ink: #333333;
    --accent-blue: #1670c4;
    --mark-grey: #4a4d52;
  }
  * { margin: 0; padding: 0; box-sizing: border-box; }
  html, body {
    width: 1200px;
    height: 734px;
    overflow: hidden;
    background: var(--paper);
  }
  .card {
    position: relative;
    width: 1200px;
    height: 734px;
    background: linear-gradient(180deg, var(--sky-top) 0%, var(--sky-bottom) 100%);
    overflow: hidden;
    font-family: "Arimo", Arial, sans-serif;
  }
  .card__arc {
    position: absolute;
    inset: 0;
    width: 1200px;
    height: 734px;
  }
  .announcement {
    position: absolute;
    top: 0;
    left: 0;
    width: 1200px;
    text-align: center;
    color: var(--paper);
  }
  .announcement__headline {
    position: absolute;
    top: 122px;
    left: 0;
    width: 1200px;
    font-family: "Playfair Display", "Didot", serif;
    font-weight: 400;
    font-size: 104px;
    line-height: 1;
    letter-spacing: 0.22em;
    padding-left: 0.22em;
  }
  .announcement__date {
    position: absolute;
    top: 286px;
    left: 0;
    width: 1200px;
    font-size: 42px;
    line-height: 1;
    letter-spacing: 0.12em;
    padding-left: 0.12em;
  }
  .brand {
    position: absolute;
    left: 130px;
    top: 520px;
    width: 270px;
    display: flex;
    flex-direction: column;
    align-items: center;
    gap: 18px;
  }
  .brand__dot {
    width: 86px;
    height: 86px;
    border-radius: 50%;
    background: var(--accent-blue);
  }
  .brand__name {
    font-family: "Arimo", Arial, sans-serif;
    font-weight: 700;
    font-size: 34px;
    line-height: 1.1;
    color: var(--mark-grey);
    text-align: center;
  }
  .contact {
    position: absolute;
    left: 512px;
    top: 528px;
    list-style: none;
    color: var(--ink);
  }
  .contact__name {
    font-weight: 700;
    font-size: 32px;
    line-height: 1;
    color: var(--accent-blue);
    margin-bottom: 24px;
  }
  .contact__line {
    font-size: 28px;
    line-height: 1;
    margin-bottom: 17px;
  }
</style>
</head>
<body>
  <main class="card">
    <svg class="card__arc" viewBox="0 0 1200 734" aria-hidden="true">
      <path d="M0,734 L0,565 Q600,235 1200,565 L1200,734 Z" fill="var(--paper)"/>
    </svg>

    <header class="announcement">
      <h1 class="announcement__headline">COMING SOON</h1>
      <p class="announcement__date">01.10.2016</p>
    </header>

    <div class="brand">
      <span class="brand__dot" aria-hidden="true"></span>
      <span class="brand__name">Brightfold Church</span>
    </div>

    <ul class="contact">
      <li class="contact__name">Owen Haller</li>
      <li class="contact__line">thebrightfoldchurch.com</li>
      <li class="contact__line">facebook.com/brightfoldchurchfm</li>
      <li class="contact__line">@HallerOw</li>
    </ul>
  </main>
</body>
</html>
```